Banner 34"x81"

This is for a Pull Up Banner
I am supplying a sample of my logo and some of my art work for you to incorporate into an upright banner.
Please business name:LuellaRo OpenHarbor Psychotherapy
phone number: 583-214-9067 NOT THE ONE ON THE BUSINESS CARD

```html
<!DOCTYPE html>
<html lang="en">
<head>
<meta charset="utf-8">
<title>LuellaRo OpenHarbor Psychotherapy – Pull Up Banner</title>
<link rel="stylesheet" href="https://fonts.googleapis.com/css2?family=Barlow:wght@500;600;700&family=Barlow+Semi+Condensed:wght@600;700&display=swap">
<style>
  :root {
    --page-bg: #a9a9a9;
    --banner-deep: #1c0a33;
    --banner-mid: #3a1462;
    --banner-violet: #4a1f7e;
    --accent-blue: #2a7de1;
    --line-blue: #1f6ee8;
    --text-light: #ffffff;
    --photo-top: #2a2f8a;
    --photo-bottom: #1d4fc4;
  }
  * { box-sizing: border-box; margin: 0; padding: 0; }
  html, body {
    width: 1200px;
    height: 800px;
    overflow: hidden;
    background: var(--page-bg);
  }
  .canvas {
    position: relative;
    width: 1200px;
    height: 800px;
    display: flex;
    align-items: center;
    justify-content: center;
  }
  .banner {
    position: relative;
    width: 320px;
    height: 760px;
    overflow: hidden;
    color: var(--text-light);
    background:
      radial-gradient(ellipse at 30% 45%, var(--banner-violet) 0%, transparent 60%),
      radial-gradient(ellipse at 70% 15%, var(--banner-mid) 0%, transparent 55%),
      linear-gradient(180deg, var(--banner-deep) 0%, var(--banner-mid) 50%, var(--banner-deep) 100%);
    font-family: "Barlow", sans-serif;
    text-align: center;
  }
  .brand-mark {
    position: absolute;
    top: 40px;
    left: 0;
    right: 0;
    display: flex;
    align-items: center;
    justify-content: center;
    gap: 8px;
    font-family: "Barlow", sans-serif;
    font-weight: 600;
    font-size: 22px;
    letter-spacing: 2px;
    color: var(--text-light);
  }
  .brand-mark__square {
    width: 14px;
    height: 14px;
    border: 2px solid var(--text-light);
  }
  .practice-name {
    position: absolute;
    top: 112px;
    left: 0;
    right: 0;
    font-weight: 500;
    font-size: 42px;
    letter-spacing: 1px;
    line-height: 1;
  }
  .practice-tagline {
    position: absolute;
    top: 168px;
    left: 0;
    right: 0;
    font-weight: 500;
    font-size: 25px;
    letter-spacing: 0.5px;
    line-height: 1;
  }
  .service-label {
    position: absolute;
    top: 218px;
    left: 35px;
    width: 250px;
    height: 42px;
    background: var(--accent-blue);
    font-family: "Barlow Semi Condensed", sans-serif;
    font-weight: 700;
    font-size: 29px;
    line-height: 42px;
    letter-spacing: 0.5px;
  }
  .phone {
    position: absolute;
    top: 272px;
    left: 0;
    right: 0;
    font-family: "Barlow Semi Condensed", sans-serif;
    font-weight: 700;
    font-size: 31px;
    letter-spacing: 1px;
  }
  .contact-row {
    position: absolute;
    left: 0;
    right: 0;
    display: flex;
    justify-content: center;
    align-items: center;
    gap: 6px;
    font-family: "Barlow Semi Condensed", sans-serif;
    font-weight: 600;
    font-size: 11.5px;
  }
  .contact-row--social { top: 330px; }
  .contact-row--email { top: 356px; }
  .contact-item {
    display: inline-flex;
    align-items: center;
    gap: 4px;
  }
  .contact-dot {
    width: 12px;
    height: 12px;
    border-radius: 50%;
    background: var(--accent-blue);
    flex: none;
  }
  .accent-lines {
    position: absolute;
    left: 0;
    top: 0;
    width: 320px;
    height: 760px;
  }
  .portrait {
    position: absolute;
    left: 42px;
    top: 398px;
    width: 240px;
    height: 362px;
    border-radius: 110px 110px 0 0;
    background: linear-gradient(180deg, var(--photo-top) 0%, var(--photo-bottom) 60%, #3c4a8a 100%);
  }
</style>
</head>
<body>
  <main class="canvas">
    <section class="banner" aria-label="LuellaRo OpenHarbor Psychotherapy pull up banner">
      <div class="brand-mark">
        <span class="brand-mark__square" aria-hidden="true"></span>
        <span class="brand-mark__name">LuellaRo</span>
      </div>

      <h1 class="practice-name">LuellaRo</h1>
      <p class="practice-tagline">OpenHarbor</p>
      <p class="service-label">PSYCHOTHERAPY</p>
      <p class="phone">583-214-9067</p>

      <div class="contact-row contact-row--social">
        <span class="contact-item"><span class="contact-dot" aria-hidden="true"></span>@LuellaOpenHarbor</span>
        <span class="contact-item"><span class="contact-dot" aria-hidden="true"></span>@LuellaHarbor</span>
      </div>
      <div class="contact-row contact-row--email">
        <span class="contact-item">
          <svg class="contact-icon" width="13" height="13" viewBox="0 0 13 13" aria-hidden="true">
            <circle cx="6.5" cy="6.5" r="6.5" fill="var(--accent-blue)"/>
            <rect x="3.2" y="4.3" width="6.6" height="4.6" fill="none" stroke="#fff" stroke-width="0.9"/>
            <polyline points="3.2,4.3 6.5,6.9 9.8,4.3" fill="none" stroke="#fff" stroke-width="0.9"/>
          </svg>
          LuellaOpenHarbor@harbormail.com
        </span>
      </div>

      <svg class="accent-lines" viewBox="0 0 320 760" aria-hidden="true">
        <polygon points="302,408 10,556 58,762" fill="none" stroke="var(--line-blue)" stroke-width="4" stroke-linejoin="miter"/>
      </svg>

      <div class="portrait" role="img" aria-label="Portrait photo of the therapist seated, wearing a blue sweater"></div>
    </section>
  </main>
</body>
</html>
```